New Powerpoint template for renewable energy company

I am looking for someone to design a .ppt file for a new renewable energy venture. Here are the critical needs:

- a well-designed cover page
- a well-designed section divider
- a well-designed working page(s)
- a well-designed back cover

I am open to your best design ideas on fonts, but to give you an example, I typically stick with Arial for most of my business work.

Lastly, theme colors are in the example colors .png file - it is from a Ridgeline Gear jacket that I own and I LOVE the colors.

Thanks and please let me know if I can answer any questions!

My best,
Jordan

```html
<!DOCTYPE html>
<html lang="en">
<head>
<meta charset="utf-8">
<title>Renewable Energy Presentation Template</title>
<link href="https://fonts.googleapis.com/css2?family=Montserrat:ital,wght@0,400;0,500;0,600;0,700;0,800;1,500&family=Open+Sans:ital,wght@0,400;0,600;1,400&family=Roboto+Slab:wght@600;700&display=swap" rel="stylesheet">
<style>
:root{
  --green:#0fc67d;
  --navy:#363e58;
  --slate:#5b6378;
  --ink:#2b2f3a;
  --muted:#7b8190;
  --sky:#a7c4d9;
  --paper:#ffffff;
  --board:#dcdde0;
}
*{margin:0;padding:0;box-sizing:border-box}
html,body{width:1053px;height:1200px;overflow:hidden;background:var(--board)}
body{position:relative;font-family:"Open Sans",Arial,sans-serif;color:var(--ink)}
.slide{position:absolute;width:314px;height:176px;background:var(--paper);overflow:hidden;box-shadow:0 2px 5px rgba(0,0,0,.22)}
.a{position:absolute}
.h{font-family:"Montserrat",Arial,sans-serif;font-weight:700;color:var(--ink);line-height:1.1}
.slab{font-family:"Roboto Slab",Georgia,serif;font-weight:700}
.tx{font-size:3.2px;line-height:1.35;color:var(--muted)}
.tw{font-size:3.2px;line-height:1.35;color:#fff}
.bar{height:1.6px;width:16px;background:var(--green)}
.green{color:var(--green)}
.photo{position:absolute}
.ph-sunset{background:linear-gradient(180deg,#7d8aa0 0%,#e9b27a 45%,#d88f4b 60%,#3f4e5c 75%,#2a3a4f 100%)}
.ph-sky{background:linear-gradient(180deg,#6f97c4 0%,#b9d2e8 55%,#3f5f8a 75%,#24406b 100%)}
.ph-field{background:linear-gradient(180deg,#3f7fc6 0%,#a7c9e8 45%,#6f9a5a 60%,#2c4a86 70%,#1d3463 100%)}
.ph-office{background:linear-gradient(135deg,#d9dde2 0%,#8c94a0 45%,#3b414d 70%,#b9c2cc 100%)}
.ph-bulb{background:radial-gradient(circle at 50% 45%,#f5d67a 0%,#7a8a3a 35%,#2c3a1e 75%)}
.ph-grey{background:linear-gradient(180deg,#d8dadd 0%,#eeeff0 60%,#c9cbcf 100%)}
.ph-dark{background:linear-gradient(180deg,#3b4460 0%,#4d5670 50%,#2f3750 100%)}
.foot{position:absolute;left:7px;right:7px;bottom:4px;display:flex;align-items:center;gap:3px;font-size:2.6px;color:var(--ink)}
.foot .url{letter-spacing:.6px}
.foot .rule{flex:1;height:.4px;background:var(--green)}
.foot .pg{background:var(--green);color:#fff;width:4.5px;height:4.5px;display:flex;align-items:center;justify-content:center;font-weight:700}
.foot.light{color:#e8eaf0}
.sq{width:7px;height:7px;background:var(--navy)}
.list .n{font-family:"Montserrat",Arial,sans-serif;font-size:5px;font-weight:500;color:#e9ebf0}
.list .n.on{color:var(--green)}
.list p{font-size:2.8px;color:#c9cdd8;margin:1px 0 6px 7px;line-height:1.3}
.disc{background:var(--green);color:#fff;font-family:"Montserrat",Arial,sans-serif;font-weight:700;font-size:12px;display:flex;align-items:center;justify-content:center}
.tbl{border:.4px solid #99a}
.tbl .th{background:var(--green);height:4px}
.tbl .rows{height:calc(100% - 4px);background:repeating-linear-gradient(180deg,#fff 0 2.6px,#c9ccd3 2.6px 3px)}
.icon-sq{width:17px;height:17px;background:var(--green);display:flex;align-items:center;justify-content:center}
</style>
</head>
<body>

<!-- 1 Cover -->
<section class="slide" style="left:44px;top:41px">
  <div class="a sq" style="left:8px;top:7px"></div>
  <div class="a h" style="left:19px;top:45px;font-size:7.5px;font-weight:500">Presentation</div>
  <div class="a h green" style="left:19px;top:53px;font-size:19px;font-weight:800">Business</div>
  <div class="a h" style="left:19px;top:75px;font-size:12px;font-weight:500">Marketing</div>
  <div class="a" style="left:19px;top:109px;font-family:Montserrat,sans-serif;font-style:italic;font-weight:500;font-size:8px;color:var(--sky)">Presentation</div>
  <div class="a" style="left:19px;top:120px;width:95px;font-size:3.6px;font-style:italic;color:var(--muted)">Lorem ipsum dolor sit amet, consectetuer adipiscing elit, sed diam nonum</div>
  <div class="a" style="left:20px;top:157px;display:flex;gap:3px"><i style="width:3px;height:3px;border-radius:50%;background:var(--navy)"></i><i style="width:3px;height:3px;border-radius:50%;background:var(--green)"></i><i style="width:3px;height:3px;border-radius:50%;background:var(--navy)"></i></div>
  <div class="photo ph-sunset" style="left:132px;top:0;width:182px;height:143px" role="img" aria-label="Wind turbines and solar panels beside a power plant at sunset"></div>
  <div class="a" style="left:132px;top:143px;width:182px;height:33px;background:var(--green);color:#fff;font-family:Montserrat,sans-serif;font-size:5px;letter-spacing:2px;display:flex;align-items:center;justify-content:center">www.website.com</div>
</section>

<!-- 2 Cover alt -->
<section class="slide" style="left:371px;top:41px">
  <div class="a sq" style="left:8px;top:7px"></div>
  <div class="a" style="left:197px;top:0;width:117px;height:25px;background:var(--green)"></div>
  <div class="a" style="left:104px;top:155px;width:210px;height:21px;background:var(--navy)"></div>
  <div class="a" style="left:128px;top:16px;width:186px;height:147px;background:#fff"></div>
  <div class="photo ph-office" style="left:131px;top:18px;width:164px;height:142px" role="img" aria-label="Smiling businesswoman holding a small solar panel at her desk"></div>
  <div class="a" style="left:288px;top:22px;width:6px;height:6px;background:#fff"></div>
  <div class="a h" style="left:22px;top:41px;font-size:7px;font-weight:500">Presentation</div>
  <div class="a h green" style="left:22px;top:49px;font-size:18px;font-weight:800">Business</div>
  <div class="a h" style="left:22px;top:69px;font-size:12px;font-weight:600">Marketing</div>
  <div class="a" style="left:18px;top:95px;width:137px;height:33px;background:var(--sky);padding:4px 4px">
    <div style="font-family:Montserrat,sans-serif;font-weight:600;font-size:7.5px;color:#fff">Presentation</div>
    <div style="font-size:3.6px;font-style:italic;color:#fff;margin-top:2px">Lorem ipsum dolor sit amet, consectetuer adipiscing elit, sed diam nonum</div>
  </div>
  <div class="a h" style="left:22px;top:137px;font-size:5.5px">30th May 2024</div>
  <div class="a" style="left:22px;top:158px;font-family:Montserrat,sans-serif;font-size:4.5px;letter-spacing:1.8px">www.websitecom</div>
</section>

<!-- 3 Discussion divider -->
<section class="slide ph-grey" style="left:697px;top:41px" role="img" aria-label="Soft grey view of a wind farm and road">
  <div class="a" style="left:75px;top:28px;width:188px;height:120px;background:var(--slate)"></div>
  <div class="a disc" style="left:30px;top:62px;width:83px;height:46px">Discussion:</div>
  <div class="a" style="left:35px;top:62px;width:3px;height:5px;background:var(--sky)"></div>
  <div class="a" style="left:95px;top:104px;width:3px;height:5px;background:var(--sky)"></div>
  <div class="a list" style="left:128px;top:40px;width:110px">
    <div class="n on">1. Lorem ipsum</div><p>Lorem ipsum dolor sit amet, consectetuer adipiscing elit, sed diam nonummy nibh euismod tincid</p>
    <div class="n">2. Lorem ipsum</div><p>Lorem ipsum dolor sit amet, consectetuer adipiscing elit, sed diam nonummy nibh euismod tincid</p>
    <div class="n">3. Lorem ipsum</div><p>Lorem ipsum dolor sit amet, consectetuer adipiscing elit, sed diam nonummy nibh euismod tincid</p>
    <div class="n">4. Lorem ipsum</div><p>Lorem ipsum dolor sit amet, consectetuer adipiscing elit, sed diam nonummy nibh euismod tincid</p>
  </div>
  <div class="foot"><span class="url">website.com</span><i class="rule"></i><span>Copyright © 2024 renewable energy venture. All rights reserved.</span><b class="pg">2</b></div>
</section>

<!-- 4 -->
<section class="slide" style="left:44px;top:230px">
  <div class="a h" style="left:17px;top:10px;font-size:11px;font-weight:600;line-height:1.3">Lorem Ipsum<br>Dolor Sit<br>Ametkeeper.</div>
  <div class="a bar" style="left:17px;top:58px"></div>
  <div class="a tx" style="left:17px;top:68px;width:80px;text-align:justify">Lorem ipsum dolor sit amet, consectetuer adipiscing elit, sed diam nonummy nibh euismod tincidunt ut laoreet dolore magna aliquam erat volutpat.<br><br>Ut wisi enim ad minim veniam, quis nostrud exerci tation ullamcorper suscipit lobortis nisl ut aliquip ex ea commodo consequat. Duis autem vel eum iriure dolor in hendrerit in vulputate velit esse molestie consequat.<br><br>vel illum dolore eu feugiat nulla facilisis at vero eros et accumsan et iusto odio dignissim qui blandit praesent luptatum</div>
  <div class="photo ph-sky" style="left:113px;top:0;width:201px;height:80px" role="img" aria-label="Wind turbines over solar fields at dusk"></div>
  <div class="a" style="left:142px;top:70px;width:62px;height:77px;background:var(--navy)"><div style="background:var(--green);height:19px;color:#fff;font-family:Montserrat,sans-serif;font-weight:600;font-size:9px;display:flex;align-items:center;justify-content:center">Text Here</div><div class="tw" style="padding:3px 5px;font-size:2.9px">Lorem ipsum dolor sit amet, consectetuer adipiscing elit, sed diam nonummy nibh euismod tincidunt ut laoreet dolore magna aliquam erat volutpat.<br><br>Ut wisi enim ad minim veniam, quis nostrud exerci tation ullamcorper suscipit lobortis nisl ut aliquip ex ea commodo conse</div></div>
  <div class="a" style="left:221px;top:70px;width:62px;height:77px;background:var(--navy)"><div style="background:var(--green);height:19px;color:#fff;font-family:Montserrat,sans-serif;font-weight:600;font-size:9px;display:flex;align-items:center;justify-content:center">Text Here</div><div class="tw" style="padding:3px 5px;font-size:2.9px">Lorem ipsum dolor sit amet, consectetuer adipiscing elit, sed diam nonummy nibh euismod tincidunt ut laoreet dolore magna aliquam erat volutpat.<br><br>Ut wisi enim ad minim veniam, quis nostrud exerci tation ullamcorper suscipit lobortis nisl ut aliquip ex ea commodo conse</div></div>
  <div class="foot"><span class="url">website.com</span><i class="rule"></i><span>Copyright © 2024 renewable energy venture. All rights reserved.</span><b class="pg">3</b></div>
</section>

<!-- 5 -->
<section class="slide" style="left:371px;top:230px">
  <div class="a h" style="left:0;width:314px;text-align:center;top:15px;font-size:11px;font-weight:600">Text Added Here</div>
  <div class="a bar" style="left:149px;top:31px"></div>
  <div class="a tx" style="left:35px;top:40px;width:244px;text-align:center">Lorem ipsum dolor sit amet, consectetuer adipiscing elit, sed diam nonummy nibh euismod tincidunt ut laoreet dolore magna aliquam erat volutpat.<br><br>Ut wisi enim ad minim veniam, quis nostrud exerci tation ullamcorper suscipit lobortis nisl ut aliquip ex ea commodo consequat. Duis autem vel eum iriure dolor in hendrerit i</div>
  <div class="a" style="left:27px;top:81px;width:83px;height:63px;background:var(--green);padding:9px 7px"><div class="slab" style="color:#fff;font-size:7.5px">Text Here</div><div class="tw" style="margin-top:3px">Lorem ipsum dolor sit amet, consectetuer adipiscing elit, sed diam nonummy nibh euismod tincidunt ut laoreet dolore magna aliquam erat volutpat.</div></div>
  <div class="photo ph-bulb" style="left:110px;top:81px;width:92px;height:63px" role="img" aria-label="Glowing light bulb with seedling beside solar panels"></div>
  <div class="a" style="left:202px;top:81px;width:83px;height:63px;background:var(--navy);padding:9px 7px"><div class="slab" style="color:#fff;font-size:7.5px">Text Here</div><div class="tw" style="margin-top:3px">Lorem ipsum dolor sit amet, consectetuer adipiscing elit, sed diam nonummy nibh euismod tincidunt ut laoreet dolore magna aliquam erat volutpat.</div></div>
  <div class="foot"><span class="url">website.com</span><i class="rule"></i><span>Copyright © 2024 renewable energy venture. All rights reserved.</span><b class="pg">4</b></div>
</section>

<!-- 6 -->
<section class="slide" style="left:697px;top:230px">
  <div class="a h" style="left:14px;top:9px;font-size:11px;font-weight:600">Text Added Here</div>
  <div class="a bar" style="left:14px;top:24px"></div>
  <div class="a" style="left:24px;top:36px;width:278px">
    <div class="h" style="font-size:6px;font-weight:600"><span class="green">1.</span> Text Added Here</div>
    <div class="tx" style="margin:2px 0 8px;color:#6e7482">Lorem ipsum dolor sit amet, cons ectetuer adipiscing elit, sed diam nonummy nibh euismod tincidunt ut laoreet dolore magna aliquam erat volutpat. Ut wisi enim ad minim veniam, quis nostrud exerci tation ullamcorper suscipit lobortis nisl ut aliquip ex ea commodo consequat. Lorem ipsum dolor sit amet, consectetuer adipiscing elit, sed diam nonummy nibh euismod tincidunt ut laoreet dolore magna aliquam erat volutpat.</div>
    <div class="h" style="font-size:6px;font-weight:600"><span class="green">2.</span> Text Added Here</div>
    <div class="tx" style="margin:2px 0 8px;color:#6e7482">Lorem ipsum dolor sit amet, cons ectetuer adipiscing elit, sed diam nonummy nibh euismod tincidunt ut laoreet dolore magna aliquam erat volutpat. Ut wisi enim ad minim veniam, quis nostrud exerci tation ullamcorper suscipit lobortis nisl ut aliquip ex ea commodo consequat. Lorem ipsum dolor sit amet, consectetuer adipiscing elit, sed diam nonummy nibh euismod tincidunt ut laoreet dolore magna aliquam erat volutpat.</div>
    <div class="h" style="font-size:6px;font-weight:600"><span class="green">3.</span> Text Added Here</div>
    <div class="tx" style="margin-top:2px;color:#6e7482">Lorem ipsum dolor sit amet, cons ectetuer adipiscing elit, sed diam nonummy nibh euismod tincidunt ut laoreet dolore magna aliquam erat volutpat. Ut wisi enim ad minim veniam, quis nostrud exerci tation ullamcorper suscipit lobortis nisl ut aliquip ex ea commodo consequat. Lorem ipsum dolor sit amet, consectetuer adipiscing elit, sed diam nonummy nibh euismod tincidunt ut laoreet dolore magna aliquam erat volutpat.</div>
  </div>
  <div class="foot"><span class="url">website.com</span><i class="rule"></i><span>Copyright © 2024 renewable energy venture. All rights reserved.</span><b class="pg">5</b></div>
</section>

<!-- 7 -->
<section class="slide" style="left:44px;top:418px">
  <div class="a h" style="left:10px;top:8px;font-size:12px;font-weight:600">Text Here</div>
  <div class="a bar" style="left:10px;top:25px"></div>
  <div class="a" style="left:31px;top:38px;width:120px">
    <div class="h" style="font-size:4.8px;font-weight:600"><span class="green" style="margin-right:2px">01.</span>Aliquam Erat Volutpat</div><div class="tx" style="margin:1px 0 11px 13px">Lorem ipsum dolor sit amet, consectetuer adipiscing elit, sed diam nonummy nibh euismod</div>
    <div class="h" style="font-size:4.8px;font-weight:600"><span class="green" style="margin-right:2px">02.</span>Consectetuer Adipiscing Elit</div><div class="tx" style="margin:1px 0 11px 13px">Lorem ipsum dolor sit amet, consectetuer adipiscing elit, sed diam nonummy nibh euismod tincidunt ut laoreet</div>
    <div class="h" style="font-size:4.8px;font-weight:600"><span class="green" style="margin-right:2px">03.</span>Duis Autem Vel Eum</div><div class="tx" style="margin:1px 0 11px 13px">Lorem ipsum dolor sit amet, consectetuer adipiscing elit, sed diam nonummy nibh euismod tincidunt.</div>
    <div class="h" style="font-size:4.8px;font-weight:600"><span class="green" style="margin-right:2px">04.</span>Aliquam Erat Volutpat</div><div class="tx" style="margin:1px 0 0 13px">Lorem ipsum dolor sit amet, consectetuer adipiscing elit, sed diam nonummy nibh euismod tincidunt ut laoreet.</div>
  </div>
  <div class="a" style="left:179px;top:36px;width:109px;height:112px;background:var(--green)"></div>
  <div class="a" style="left:198px;top:45px;width:86px">
    <div class="h" style="color:#fff;font-size:6.5px;font-weight:600">Lorem ipsum</div><div class="tw" style="margin:1px 0 15px">ipsum dolor sit amet, cons ectetuer adipiscing elit, sed diam nonummy nibh euismod tincidunt ut laoreet</div>
    <div class="h" style="color:#fff;font-size:6.5px;font-weight:600">Lorem ipsum</div><div class="tw" style="margin:1px 0 15px">ipsum dolor sit amet, cons ectetuer adipiscing elit, sed diam nonummy nibh euismod tincidunt ut laoreet</div>
    <div class="h" style="color:#fff;font-size:6.5px;font-weight:600">Lorem ipsum</div><div class="tw" style="margin-top:1px">ipsum dolor sit amet, cons ectetuer adipiscing elit, sed diam nonummy nibh euismod tincidunt</div>
  </div>
  <svg class="a" style="left:166px;top:44px" width="26" height="102" viewBox="0 0 26 102">
    <g fill="var(--navy)" stroke="#fff" stroke-width="1.5"><circle cx="13" cy="13" r="12"/><circle cx="13" cy="51" r="12"/><circle cx="13" cy="89" r="12"/></g>
    <g fill="none" stroke="#fff" stroke-width="1"><rect x="7" y="8" width="12" height="8" rx="1"/><path d="M11 19h4M13 16v3"/>
    <path d="M8 53a4 4 0 0 1 2-7a5 5 0 0 1 9 2a3 3 0 0 1 0 5z"/><path d="M11 53v4M15 53v4"/>
    <circle cx="8" cy="93" r="1.8"/><circle cx="13" cy="85" r="1.8"/><circle cx="19" cy="90" r="1.8"/><path d="M9 92l3-6M14 86l4 3"/></g>
  </svg>
  <div class="foot"><span class="url">website.com</span><i class="rule"></i><span>Copyright © 2024 renewable energy venture. All rights reserved.</span><b class="pg">6</b></div>
</section>

<!-- 8 Discussion dark -->
<section class="slide ph-dark" style="left:371px;top:418px" role="img" aria-label="Dark blue view of a wind farm and road">
  <div class="a" style="left:75px;top:28px;width:188px;height:120px;background:var(--navy)"></div>
  <div class="a disc" style="left:29px;top:67px;width:84px;height:40px">Discussion:</div>
  <div class="a" style="left:35px;top:63px;width:3px;height:5px;background:var(--sky)"></div>
  <div class="a" style="left:92px;top:105px;width:3px;height:5px;background:var(--sky)"></div>
  <div class="a list" style="left:128px;top:40px;width:110px">
    <div class="n">1. Lorem ipsum</div><p>Lorem ipsum dolor sit amet, consectetuer adipiscing elit, sed diam nonummy nibh euismod tincid</p>
    <div class="n on">2. Lorem ipsum</div><p>Lorem ipsum dolor sit amet, consectetuer adipiscing elit, sed diam nonummy nibh euismod tincid</p>
    <div class="n">3. Lorem ipsum</div><p>Lorem ipsum dolor sit amet, consectetuer adipiscing elit, sed diam nonummy nibh euismod tincid</p>
    <div class="n">4. Lorem ipsum</div><p>Lorem ipsum dolor sit amet, consectetuer adipiscing elit, sed diam nonummy nibh euismod tincid</p>
  </div>
  <div class="foot light"><span class="url">website.com</span><i class="rule"></i><span>Copyright © 2024 renewable energy venture. All rights reserved.</span><b class="pg">7</b></div>
</section>

<!-- 9 -->
<section class="slide" style="left:697px;top:418px">
  <div class="a h" style="left:15px;top:14px;font-size:12px;font-weight:600;line-height:1.2">Text<br>Added<br>Here</div>
  <div class="a bar" style="left:15px;top:67px;width:12px"></div>
  <div class="a tx" style="left:15px;top:73px;width:45px">Lorem ipsum dolor sit amet, consec-tetuer adipiscing elit, sed diam nonummy nibh euismod tincidunt ut laoreet dolore magna aliquam erat volutpat.<br><br>Ut wisi enim ad minim veniam, quis nostrud exerci tation ullamcorper suscipit lobortis nisl ut aliquip ex ea commodo</div>
  <div class="photo ph-field" style="left:68px;top:0;width:112px;height:176px" role="img" aria-label="Wind turbine above a large solar farm"></div>
  <div class="a" style="left:168px;top:30px;width:140px">
    <div style="display:flex;gap:7px;margin-bottom:24px"><div class="icon-sq" style="margin-top:2px"><svg width="11" height="9" viewBox="0 0 11 9" fill="#fff"><circle cx="5.5" cy="2" r="1.8"/><circle cx="2" cy="3" r="1.3"/><circle cx="9" cy="3" r="1.3"/><path d="M2.5 9a3 3 0 0 1 6 0zM0 8a2 2 0 0 1 3-2l-.8 2zM11 8a2 2 0 0 0-3-2l.8 2z"/></svg></div><div><div class="h" style="font-size:6px">We Before Me</div><div class="tx" style="margin-top:1px">ipsum dolor sit amet, cons ectetuer adipiscing elit, sed diam nonummy nibh euismod tincidunt ut laoreet</div></div></div>
    <div style="display:flex;gap:7px;margin-bottom:22px"><div class="icon-sq" style="margin-top:2px"><svg width="10" height="11" viewBox="0 0 10 11" fill="#fff"><circle cx="3" cy="1.5" r="1.4"/><circle cx="7" cy="1.5" r="1.4"/><rect x="1.5" y="3.5" width="3" height="7"/><rect x="5.5" y="3.5" width="3" height="7"/></svg></div><div><div class="h" style="font-size:6px">We Are Good People</div><div class="tx" style="margin-top:1px">ipsum dolor sit amet, cons ectetuer adipiscing elit, sed diam nonummy nibh euismod ut laoreet dolore magna aliquam erat volutpat.</div></div></div>
    <div style="display:flex;gap:7px"><div class="icon-sq" style="margin-top:2px"><svg width="11" height="10" viewBox="0 0 11 10" fill="#fff"><path d="M5.5 5C3 3 2.5 1 4 .5s1.5 1 1.5 1S6.5 0 7.5.6s.8 2.4-2 4.4z"/><path d="M0 7l3-1 3 1 4-2 .8 1L6 9H2L0 9z"/></svg></div><div><div class="h" style="font-size:6px">We Work with Heart</div><div class="tx" style="margin-top:1px">ipsum dolor sit amet, cons ectetuer adipiscing elit, sed diam nonummy nibh euismod tincidunt</div></div></div>
  </div>
  <div class="foot"><span class="url">website.com</span><i class="rule"></i><span>Copyright © 2024 renewable energy venture. All rights reserved.</span><b class="pg">8</b></div>
</section>

<!-- 10 Pipeline -->
<section class="slide" style="left:44px;top:607px">
  <div class="a h" style="left:10px;top:6px;font-size:9.5px;font-weight:600">Existing Project Pipeline</div>
  <div class="a tx" style="left:10px;top:21px;width:280px;color:#6e7482">The pipeline described below only includes existing opportunities which have been discussed and modeled with prospective clients, with zero accounting for the growth in the pipeline in subsequent years.</div>
  <div class="a" style="left:60px;top:38px;font-size:2.4px;text-align:center;font-weight:600">DevCo NTP Forecast<br>Unweighted</div>
  <div class="a" style="left:193px;top:38px;font-size:2.4px;text-align:center;font-weight:600">DevCo NTP Forecast<br>Probability-weighted</div>
  <div class="a tbl" style="left:24px;top:48px;width:110px;height:52px"><div class="th"></div><div class="rows"></div></div>
  <div class="a tbl" style="left:157px;top:48px;width:123px;height:52px"><div class="th"></div><div class="rows"></div></div>
  <div class="a tbl" style="left:24px;top:98px;width:110px;height:48px"><div class="th"></div><div class="rows"></div></div>
  <div class="a tbl" style="left:157px;top:98px;width:123px;height:48px"><div class="th"></div><div class="rows"></div></div>
  <div class="a" style="left:24px;top:147px;width:110px;height:6px;border-top:.4px solid #99a"><div style="background:var(--green);width:24px;height:2px"></div></div>
  <div class="a" style="left:157px;top:147px;width:123px;height:6px;border-top:.4px solid #99a"><div style="background:var(--green);width:24px;height:2px"></div></div>
  <div class="foot"><span class="url">website.com</span><i class="rule"></i><span>Copyright © 2024 renewable energy venture. All rights reserved.</span><b class="pg">9</b></div>
</section>

<!-- 11 Utility-scale -->
<section class="slide" style="left:371px;top:607px">
  <div class="a h" style="left:11px;top:8px;font-size:9.5px;font-weight:600">Business Line: Utility-Scale Development</div>
  <div class="a bar" style="left:11px;top:22px"></div>
  <div class="a tx" style="left:11px;top:28px;width:290px;color:#6e7482">Solvane expects its future growth and ability to scale to depend meaningfully on its ability to originate, build, own, and operate distribution-net-work-interconnected utility-scale projects.</div>
  <div class="a" style="left:15px;top:50px;width:172px;font-size:3.8px;line-height:1.3;color:#555;text-align:justify"><b class="green">Strategic Rationale :</b> Regulated utilities and corporate power users have increasing demand to buy renewable power using longterm PPAs; to meet this demand a developer can secure land and approvals to build a solar project. Once built, the solar project represents a low volatility, long-term yielding asset that is both valuable and liquid to a wide universe of capital partners.</div>
  <div class="a green" style="left:13px;top:98px;font-family:Montserrat,sans-serif;font-weight:600;font-size:5px">Utility-scale Development Process</div>
  <div class="a" style="left:14px;top:107px;display:flex;gap:2px">
    <div style="width:41px;height:42px;background:var(--green);padding:2px"><div style="color:var(--navy);font-size:3.6px;font-weight:600">Market<br>Selection</div><div class="tw" style="font-size:2.3px">Ipsum dolor sit amet, cons ectetuer adipiscing elit, sed diam nonummy nibh euismod tincidunt ut laoreet</div></div>
    <div style="width:41px;height:42px;background:var(--navy);padding:2px"><div style="color:var(--green);font-size:3.6px;font-weight:600">Project<br>Development</div><div class="tw" style="font-size:2.3px">Ipsum dolor sit amet, cons ectetuer adipiscing elit, sed diam nonummy nibh euismod tincidunt ut laoreet</div></div>
    <div style="width:41px;height:42px;background:var(--green);padding:2px"><div style="color:var(--navy);font-size:3.6px;font-weight:600">Project<br>Financing</div><div class="tw" style="font-size:2.3px">Ipsum dolor sit amet, cons ectetuer adipiscing elit, sed diam nonummy nibh euismod tincidunt ut laoreet</div></div>
    <div style="width:41px;height:42px;background:var(--navy);padding:2px"><div style="color:var(--green);font-size:3.6px;font-weight:600">Construction<br>And Operations</div><div class="tw" style="font-size:2.3px">Ipsum dolor sit amet, cons ectetuer adipiscing elit, sed diam nonummy nibh euismod tincidunt ut laoreet</div></div>
  </div>
  <div class="a slab" style="left:216px;top:50px;font-size:4.3px;font-weight:600">Utility-scale Development</div>
  <div class="a" style="left:201px;top:58px;width:89px;height:89px;border:.6px solid var(--green);padding:3px"><div class="ph-sunset" style="width:100%;height:100%" role="img" aria-label="Wind turbine and solar panels at sunrise"></div></div>
  <div class="foot"><span class="url">website.com</span><i class="rule"></i><span>Copyright © 2024 renewable energy venture. All rights reserved.</span><b class="pg">10</b></div>
</section>

<!-- 12 Revenue -->
<section class="slide" style="left:697px;top:607px">
  <div class="a h" style="left:11px;top:8px;font-size:9.5px;font-weight:600">Business Line: Utility-Scale Development</div>
  <div class="a bar" style="left:11px;top:22px"></div>
  <div class="a h green" style="left:18px;top:47px;font-size:7.5px;font-weight:600">Revenue Strategy</div>
  <div class="a" style="left:20px;top:63px;width:125px">
    <div style="font-size:3.6px;font-weight:600">• Primary Revenue Strategy:</div><div class="tx" style="margin:1px 0 8px 4px">Lorem ipsum dolor sit amet, cons ectetuer adipiscing elit, sed diam nonummy nibh euismod tincidunt ut laoreet dolore magna aliquam erat volutpat. Ut wisi enim ad minim veniam,</div>
    <div style="font-size:3.6px;font-weight:600">• Secondary Revenue Strategy:</div><div class="tx" style="margin:1px 0 4px 4px">Lorem ipsum dolor sit amet, cons ectetuer adipiscing elit, sed diam nonummy nibh euismod tincidunt ut laoreet dolore magna aliquam erat volutpat. Ut wisi enim ad minim veniam.</div>
    <div class="tx" style="margin-left:4px">Lorem ipsum dolor sit amet, cons ectetuer adipiscing elit, sed diam nonummy nibh euismod tincidunt ut laoreet dolore magna aliquam erat volutpat. Ut wisi enim ad minim veniam.</div>
  </div>
  <div class="a" style="left:152px;top:44px;width:143px;height:100px;background:var(--green);padding:4px 6px">
    <div class="h" style="font-size:7.5px;font-weight:600">Revenue Strategy</div>
    <div style="font-size:3.4px;color:var(--navy);font-weight:600;margin-top:6px">• Fund and Accelerate Development:</div><div class="tw" style="margin:1px 0 5px 3px">Lorem ipsum dolor sit amet, cons ectetuer adipiscing elit, sed diam nonummy nibh euismod tincidunt ut laoreet</div>
    <div style="font-size:3.4px;color:var(--navy);font-weight:600">• Fund Permanent Project Equity:</div><div class="tw" style="margin:1px 0 5px 3px">Lorem ipsum dolor sit amet, cons ectetuer adipiscing elit, sed diam nonummy nibh euismod tincidunt ut laoreet dolore magna aliquam erat volutpat. Ut wisi enim ad minim veniam.</div>
    <div style="font-size:3.4px;color:var(--navy);font-weight:600">• Selectively Expand Development in New Markets:</div><div class="tw" style="margin:1px 0 0 3px">Lorem ipsum dolor sit amet, cons ectetuer adipiscing elit, sed diam nonummy nibh euismod tincidunt ut laoreet dolore magna aliquam erat volutpat. Ut wisi enim ad minim veniam.</div>
  </div>
  <div class="foot"><span class="url">website.com</span><i class="rule"></i><span>Copyright © 2024 renewable energy venture. All rights reserved.</span><b class="pg">11</b></div>
</section>

<!-- 13 C&I -->
<section class="slide" style="left:44px;top:795px">
  <div class="a h" style="left:10px;top:7px;font-size:9.5px;font-weight:600">Business Line: C&amp;I Development</div>
  <div class="a bar" style="left:10px;top:21px"></div>
  <table class="a" style="left:12px;top:30px;width:290px;border-collapse:collapse;font-size:3px">
    <colgroup><col style="width:45px"><col style="width:144px"><col></colgroup>
    <tr style="height:7px"><td style="background:var(--green);color:var(--navy);font-weight:700;padding-left:2px;border-bottom:.4px solid #fff">Project Size</td><td style="border-bottom:.4px solid #999;padding-left:3px">• 1,107 kWDC / 850 kWAC</td><td rowspan="5" style="border-left:.4px solid #999;position:relative"><div class="a" style="left:23px;top:2px;width:35px;height:45px;background:var(--navy);border-radius:40% 20% 30% 10%" role="img" aria-label="Map of the project state with location marker"></div><div class="a" style="left:58px;top:36px;width:32px;height:8px;background:var(--green);color:#fff;font-size:2.3px;text-align:center;line-height:1.2;padding-top:1px">Project Location<br>Portland, ME</div></td></tr>
    <tr style="height:7px"><td style="background:var(--green);color:var(--navy);font-weight:700;padding-left:2px;border-bottom:.4px solid #fff">Location</td><td style="border-bottom:.4px solid #999;padding-left:3px">• Portland, Maine</td></tr>
    <tr style="height:7px"><td style="background:var(--green);color:var(--navy);font-weight:700;padding-left:2px;border-bottom:.4px solid #fff">NTP / COD Dates</td><td style="border-bottom:.4px solid #999;padding-left:3px">• Apr-2023 / Jan-2024</td></tr>
    <tr style="height:7px"><td style="background:var(--green);color:var(--navy);font-weight:700;padding-left:2px;border-bottom:.4px solid #fff">Energy Output</td><td style="border-bottom:.4px solid #999;padding-left:3px">• 1,096 kWh/kW dc</td></tr>
    <tr style="height:20px"><td style="background:var(--green);color:var(--navy);font-weight:700;padding-left:2px;border-bottom:.4px solid #fff">Site Control</td><td style="border-bottom:.4px solid #999;padding-left:3px;line-height:1.3">• Site Control acquired, approximately 70,000 ft²<br>• 20-yr lease signed with Harbor Bay REIT real estate entity with 3 5-year extensions at the project's option<br>• Annual basic rent of $24,260 per</td></tr>
    <tr style="height:22px"><td style="background:var(--green);color:var(--navy);font-weight:700;padding-left:2px;border-bottom:.4px solid #fff">Permitting / Approvals</td><td colspan="2" style="border-bottom:.4px solid #999;padding-left:3px">• Municipal Building and Electrical</td></tr>
    <tr style="height:14px"><td style="background:var(--green);color:var(--navy);font-weight:700;padding-left:2px;border-bottom:.4px solid #fff">Interconnection</td><td colspan="2" style="border-bottom:.4px solid #999;padding-left:3px;line-height:1.4">• Interconnection Agreement executed<br>• Interconnection costs: less than $0.01/W dc</td></tr>
    <tr style="height:7px"><td style="background:var(--green);color:var(--navy);font-weight:700;padding-left:2px">EPC</td><td colspan="2" style="border-bottom:.4px solid #999;padding-left:3px">• Total EPC costs: $1.74 / W dc</td></tr>
  </table>
  <div class="a tx" style="left:15px;top:129px;width:284px;text-align:center;color:#555">Lorem ipsum dolor sit amet, consectetuer adipiscing elit, sed diam nonummy nibh euismod tincidunt ut laoreet dolore magna aliquam erat volutpat. Ut wisi enim ad minim veniam, quis nostrud exerci tation ullamcorper suscipit lobortis nisl ut aliquip ex ea commodo consequat. Duis autem vel eum iriure dolor in hendrerit in vulputate velit esse molestie consequat.</div>
  <div class="foot"><span class="url">website.com</span><i class="rule"></i><span>Copyright © 2024 renewable energy venture. All rights reserved.</span><b class="pg">13</b></div>
</section>

<!-- 14 Cycle -->
<section class="slide" style="left:371px;top:795px">
  <div class="a h" style="left:11px;top:6px;font-size:12px;font-weight:600">Text Added Here</div>
  <div class="a bar" style="left:11px;top:23px"></div>
  <svg class="a" style="left:112px;top:47px" width="90" height="90" viewBox="0 0 90 90">
    <path d="M45 45V2A43 43 0 0 1 88 45z" fill="var(--green)"/>
    <path d="M45 45H88A43 43 0 0 1 45 88z" fill="var(--navy)"/>
    <path d="M45 45V88A43 43 0 0 1 2 45z" fill="var(--green)"/>
    <path d="M45 45H2A43 43 0 0 1 45 2z" fill="var(--navy)"/>
    <path d="M45 2v86M2 45h86" stroke="#fff" stroke-width="1.5"/>
    <circle cx="45" cy="45" r="21" fill="#fff"/>
    <g fill="none" stroke="#fff" stroke-width="1"><circle cx="22" cy="22" r="4"/><circle cx="22" cy="22" r="1.5"/><path d="M64 25l6-6M66 19h4v4"/><rect x="18" y="64" width="7" height="6"/><circle cx="68" cy="68" r="4"/><path d="M68 68l4-4"/></g>
  </svg>
  <div class="a slab" style="left:135px;top:81px;width:44px;text-align:center;font-size:7px;line-height:1.2">Text<br>Added</div>
  <div class="a" style="left:38px;top:48px;width:68px;text-align:center"><div class="slab green" style="font-size:5px">Text Here</div><div class="tx">Lorem ipsum dolor sit amet, consectetuer adipiscing elit, sed diammy nibh euismod tincidunt ut laoreet dolore</div></div>
  <div class="a" style="left:38px;top:108px;width:68px;text-align:center"><div class="slab" style="font-size:5px">Text Here</div><div class="tx">Lorem ipsum dolor sit amet, consectetuer adipiscing elit, sed diammy nibh euismod tincidunt ut laoreet dolore</div></div>
  <div class="a" style="left:204px;top:48px;width:68px"><div class="slab" style="font-size:5px">Text Here</div><div class="tx">Lorem ipsum dolor sit amet, consectetuer adipiscing elit, sed diammy nibh euismod tincidunt ut laoreet dolore</div></div>
  <div class="a" style="left:204px;top:108px;width:68px"><div class="slab green" style="font-size:5px">Text Here</div><div class="tx">Lorem ipsum dolor sit amet, consectetuer adipiscing elit, sed diammy nibh euismod tincidunt ut laoreet dolore</div></div>
  <div class="foot"><span class="url">website.com</span><i class="rule"></i><span>Copyright © 2024 renewable energy venture. All rights reserved.</span><b class="pg">14</b></div>
</section>

<!-- 15 Timeline -->
<section class="slide" style="left:697px;top:795px">
  <div class="a h" style="left:11px;top:6px;font-size:12px;font-weight:600">Text Added Here</div>
  <div class="a bar" style="left:11px;top:23px"></div>
  <svg class="a" style="left:20px;top:30px" width="280" height="110" viewBox="0 0 280 110">
    <g font-family="Montserrat,Arial,sans-serif" font-size="4.5" font-weight="700" fill="#fff" text-anchor="middle">
      <polygon points="0,60 46,60 51,69 5,69" fill="var(--navy)"/>
      <polygon points="53,60 99,60 104,69 58,69" fill="var(--green)"/>
      <polygon points="106,60 152,60 157,69 111,69" fill="var(--navy)"/>
      <polygon points="159,60 205,60 210,69 164,69" fill="var(--green)"/>
      <polygon points="212,60 258,60 263,69 217,69" fill="var(--navy)"/>
      <text x="26" y="66">1990</text><text x="79" y="66">2001</text><text x="132" y="66">2007</text><text x="185" y="66">2012</text><text x="238" y="66">2020</text>
    </g>
    <g stroke="var(--navy)" stroke-width="1" fill="var(--navy)"><line x1="26" y1="40" x2="26" y2="52"/><circle cx="26" cy="52" r="2"/><line x1="132" y1="40" x2="132" y2="52"/><circle cx="132" cy="52" r="2"/><line x1="238" y1="40" x2="238" y2="52"/><circle cx="238" cy="52" r="2"/></g>
    <g stroke="var(--green)" stroke-width="1" fill="var(--green)"><line x1="79" y1="74" x2="79" y2="86"/><circle cx="79" cy="86" r="2"/><line x1="185" y1="74" x2="185" y2="86"/><circle cx="185" cy="86" r="2"/></g>
    <g text-anchor="middle" font-size="3.6" fill="#7b8190" font-family="Open Sans,Arial,sans-serif">
      <text x="26" y="19" font-family="Roboto Slab,serif" font-weight="700" font-size="4.6" fill="#2b2f3a">Your Title</text><text x="26" y="25">Refers to a good or</text><text x="26" y="30">service being offered</text>
      <text x="132" y="19" font-family="Roboto Slab,serif" font-weight="700" font-size="4.6" fill="#2b2f3a">Your Title</text><text x="132" y="25">Refers to a good or</text><text x="132" y="30">service being offered</text>
      <text x="238" y="19" font-family="Roboto Slab,serif" font-weight="700" font-size="4.6" fill="#2b2f3a">Your Title</text><text x="238" y="25">Refers to a good or</text><text x="238" y="30">service being offered</text>
      <text x="79" y="97" font-family="Roboto Slab,serif" font-weight="700" font-size="4.6" fill="var(--green)">Your Title</text><text x="79" y="102">Refers to a good or</text><text x="79" y="107">service being offered</text>
      <text x="185" y="97" font-family="Roboto Slab,serif" font-weight="700" font-size="4.6" fill="var(--green)">Your Title</text><text x="185" y="102">Refers to a good or</text><text x="185" y="107">service being offered</text>
    </g>
  </svg>
  <div class="foot"><span class="url">website.com</span><i class="rule"></i><span>Copyright © 2024 renewable energy venture. All rights reserved.</span><b class="pg">15</b></div>
</section>

<!-- 16 -->
<section class="slide" style="left:44px;top:984px">
  <div class="a h" style="left:10px;top:6px;font-size:12px;font-weight:600">Text Added Here</div>
  <div class="a bar" style="left:10px;top:23px"></div>
  <div class="photo ph-field" style="left:21px;top:48px;width:65px;height:37px" role="img" aria-label="Solar panels in a field under blue sky"></div>
  <div class="photo ph-sky" style="left:99px;top:48px;width:65px;height:37px" role="img" aria-label="Wind turbines behind a solar array"></div>
  <div class="a" style="left:21px;top:90px;width:65px"><div class="slab" style="font-size:5.5px">Text Here</div><div class="tx" style="font-size:2.6px">Lorem ipsum dolor sit amet, consectetuer adipiscing elit, sed diam nonummy nibh euismod tincidunt ut laoreet dolore magna aliquam erat volutpat.<br><br>Lorem ipsum dolor sit amet, consectetuer adipiscing elit, sed diam nonummy nibh euismod tincidunt ut laoreet dolore magna aliquam erat volutpat dolor sit amet</div></div>
  <div class="a" style="left:99px;top:90px;width:65px"><div class="slab" style="font-size:5.5px">Text Here</div><div class="tx" style="font-size:2.6px">Lorem ipsum dolor sit amet, consectetuer adipiscing elit, sed diam nonummy nibh euismod tincidunt ut laoreet dolore magna aliquam erat volutpat.<br><br>Lorem ipsum dolor sit amet, consectetuer adipiscing elit, sed diam nonummy nibh euismod tincidunt ut laoreet dolore magna aliquam erat volutpat dolor sit amet</div></div>
  <div class="a h" style="left:182px;top:47px;font-size:14px;font-weight:600;line-height:1.15">Lorem Ipsum<br>Dolor Sit<br>Ametkeeper.</div>
  <div class="a" style="left:175px;top:105px;width:113px;height:29px;background:var(--green);padding:4px 7px"><div class="tw" style="font-size:4px">Lorem ipsum dolor sit amet, consectetuer adipiscing elit, sed diam euismod tincidunt ut laoreet dolore magna aliquam.</div></div>
  <div class="foot"><span class="url">website.com</span><i class="rule"></i><span>Copyright © 2024 renewable energy venture. All rights reserved.</span><b class="pg">16</b></div>
</section>

<!-- 17 Team -->
<section class="slide" style="left:371px;top:984px">
  <div class="a h" style="left:11px;top:6px;font-size:12px;font-weight:600">Our Team Members</div>
  <div class="a bar" style="left:11px;top:23px"></div>
  <div class="a" style="left:28px;top:52px;width:260px;display:flex;justify-content:space-between">
    <div style="width:46px;text-align:center;position:relative"><div style="height:11px;background:var(--green)"></div><div role="img" aria-label="Portrait of team member" style="position:absolute;left:11px;top:2px;width:24px;height:24px;border-radius:50%;background:#c9ccd2;border:1.5px solid #fff"></div><div class="h green" style="font-size:5px;margin-top:20px">OWEN HALE</div><div class="tx" style="font-size:2.7px;margin-top:2px">Lorem ipsum dolor sit amet, cons ectetuer adipiscing elit, sed diam nonummy nibh euismod tincidunt<br><br>ut laoreet dolore magna aliquam erat volutpat. Ut wisi enim ad minim veniam, quis nostrud</div></div>
    <div style="width:46px;text-align:center;position:relative"><div style="height:11px;background:var(--navy)"></div><div role="img" aria-label="Portrait of team member" style="position:absolute;left:11px;top:2px;width:24px;height:24px;border-radius:50%;background:#c9ccd2;border:1.5px solid #fff"></div><div class="h" style="font-size:5px;margin-top:20px">NORA VANCE</div><div class="tx" style="font-size:2.7px;margin-top:2px">Lorem ipsum dolor sit amet, cons ectetuer adipiscing elit, sed diam nonummy nibh euismod tincidunt<br><br>aliquam erat volutpat. Ut wisi enim ad minim veniam, quis nostrud</div></div>
    <div style="width:46px;text-align:center;position:relative"><div style="height:11px;background:var(--green)"></div><div role="img" aria-label="Portrait of team member" style="position:absolute;left:11px;top:2px;width:24px;height:24px;border-radius:50%;background:#c9ccd2;border:1.5px solid #fff"></div><div class="h green" style="font-size:5px;margin-top:20px">OWEN HALE</div><div class="tx" style="font-size:2.7px;margin-top:2px">Lorem ipsum dolor sit amet, cons ectetuer adipiscing elit, sed diam nonummy nibh euismod tincidunt<br><br>Ut wisi enim ad minim veniam, quis nostrud</div></div>
    <div style="width:46px;text-align:center;position:relative"><div style="height:11px;background:var(--navy)"></div><div role="img" aria-label="Portrait of team member" style="position:absolute;left:11px;top:2px;width:24px;height:24px;border-radius:50%;background:#c9ccd2;border:1.5px solid #fff"></div><div class="h" style="font-size:5px;margin-top:20px">NORA VANCE</div><div class="tx" style="font-size:2.7px;margin-top:2px">Lorem ipsum dolor sit amet, cons ectetuer adipiscing elit, sed diam nonummy nibh euismod tincidunt<br><br>aliquam erat volutpat. Ut wisi enim ad minim veniam, quis nostrud</div></div>
  </div>
  <div class="foot"><span class="url">website.com</span><i class="rule"></i><span>Copyright © 2024 renewable energy venture. All rights reserved.</span><b class="pg">17</b></div>
</section>

<!-- 18 Back cover -->
<section class="slide" style="left:697px;top:984px">
  <div class="photo ph-field" style="left:0;top:16px;width:146px;height:144px" role="img" aria-label="Wind turbines above a solar farm under blue sky"></div>
  <div class="a h" style="left:162px;top:48px;font-size:20px;font-weight:700">Thank You</div>
  <div class="a" style="left:162px;top:83px;font-size:4.6px;color:#555;line-height:1.25">
    <div style="display:flex;gap:5px;align-items:center;margin-bottom:8px"><svg width="8" height="8" viewBox="0 0 8 8"><path d="M1.5 .5l1.7 1.9-.8 1.2c.5 1 1 1.5 2 2l1.2-.8 1.9 1.7-1 1C3.6 7.6.4 4.4.5 1.5z" fill="var(--green)"/></svg><span style="border-left:.6px solid #555;padding-left:4px">+18 2000 5550 0101<br>+18 2000 5550 0101</span></div>
    <div style="display:flex;gap:5px;align-items:center;margin-bottom:8px"><svg width="8" height="8" viewBox="0 0 8 8"><path d="M0 3.5L8 0 5 8 4 4.5z" fill="var(--green)"/></svg><span style="border-left:.6px solid #555;padding-left:4px">www.solvane-energy.com<br>hello@solvane-energy.com</span></div>
    <div style="display:flex;gap:5px;align-items:center"><svg width="8" height="8" viewBox="0 0 8 8"><path d="M4 .5L0 4h1.2v3.5h2V5.3h1.6v2.2h2V4H8z" fill="var(--green)"/></svg><span style="border-left:.6px solid #555;padding-left:4px">88 Meadow Lane, Brookfield,<br>post/zip 040101.</span></div>
  </div>
</section>

</body>
</html>
```